nine-parts.com

We are a small dollar lending company that will revolutionize the industry. We will do this by being completely transparent, fee free, etc and an interest rate that normal people can afford to pay. Over 10X less than our competition. We only allow our members to pay bills " bills paid fast", within 72 hours. Payday loans typically charge from 390%-600% with a terrible payback structure. We charge 36%, period, with a payback structure over 12 months. Our site will be very simple and easy to use but elegant at the same time. We do not want the site to be too busy, less is more and easier. We will have; Home, The Story, Why 9parts.com, Are you eligible? Members, Clients. To become a member you have to be referred by a current client of 9parts.com. A lot of the busy stuff will be saved for the Members and Clients sections. The feel must be elegant, easy to use and very simple to understand. I am looking for the green, white and black combinations of colors, very similar to my logo that was designed by Pixelmoor.

```html
<!DOCTYPE html>
<html lang="en">
<head>
<meta charset="utf-8">
<title>nine-parts.com — Bills Paid Fast</title>
<link href="https://fonts.googleapis.com/css2?family=Arimo:wght@700&family=Open+Sans:wght@400;600;700&display=swap" rel="stylesheet">
<style>
:root{
  --green:#4cae4f;
  --green-dark:#3f9a43;
  --green-light:#5cbc5e;
  --ink:#333;
  --text:#666;
  --muted:#999;
  --line:#ddd;
  --band:#e1e8e1;
  --white:#fff;
}
*{box-sizing:border-box;margin:0;padding:0}
html,body{width:997px;height:1200px;overflow:hidden;background:var(--white);font-family:"Open Sans",sans-serif;color:var(--text)}
.page{position:relative;width:997px;height:1200px}
.wrap{width:719px;margin:0 auto;position:relative}

.site-header{height:116px;background:linear-gradient(var(--green-light),var(--green));}
.site-header .wrap{height:116px}
.brand{position:absolute;left:-2px;top:8px;text-align:center}
.brand-name{font-family:"Arimo",sans-serif;font-weight:700;font-size:25px;color:var(--white);letter-spacing:-.3px;line-height:28px}
.brand-tag{font-size:13px;color:#1f4d20}
.contact{position:absolute;right:0;top:17px;display:flex;gap:10px}
.contact div{font-size:10.5px;color:#1f4d20;line-height:13px}
.contact strong{display:block;font-weight:400;font-size:16px;color:var(--white);line-height:20px}
.contact .sep{border-left:1px solid rgba(255,255,255,.35);padding-left:8px}
.header-rule{position:absolute;left:0;right:0;top:69px;border-top:1px solid rgba(255,255,255,.25)}
.nav{position:absolute;top:82px;left:97px;display:flex;list-style:none}
.nav li{font-size:13px;font-weight:600;color:var(--white);padding:9px 15px 8px;height:34px;white-space:nowrap}
.nav li.active{background:linear-gradient(#fff,#eaf3ea);color:var(--green-dark);border:1px solid #c6dfc6;border-bottom:none;border-radius:3px 3px 0 0;padding:8px 18px}

.hero{height:161px;background:linear-gradient(100deg,#d9dde4 0%,#9aa2ad 30%,#7b8390 55%,#c9a793 75%,#bfc5cc 100%)}

.content{position:absolute;left:139px;top:0;width:719px;height:952px}
.content section{position:absolute;left:0;width:719px}
h2{font-weight:400;font-size:21px;line-height:28px;color:#555;text-align:center}
h2 .accent{color:var(--green);font-weight:600}
.welcome{top:297px}
.welcome p{font-size:10.3px;line-height:17px;margin-top:11px;text-align:justify}
.welcome p a{color:var(--ink);font-weight:600;text-decoration:none;margin-left:6px}
.btn{display:block;width:122px;height:33px;margin:16px auto 0;border:1px solid var(--green);border-radius:3px;font-size:13px;color:#555;text-align:center;line-height:31px}

.calc{top:473px}
.calc-row{display:flex;justify-content:space-between;margin-top:20px;font-size:11.5px;font-weight:600;color:var(--green);line-height:16px}
.calc-row small{display:block;font-size:9.5px;font-weight:400;color:var(--muted);line-height:12px}
.calc-notes{border-top:1px solid var(--line);border-bottom:1px solid var(--line);margin-top:6px;padding:7px 0 8px;font-size:10.3px;line-height:17px;background:linear-gradient(#fff,#fafafa)}

.features{top:650px}
.feature{position:absolute;width:216px}
.feature h3{font-size:12px;font-weight:700;color:#444;display:flex;align-items:center;gap:6px;margin-bottom:4px;white-space:nowrap;line-height:22px}
.feature p{font-size:10.3px;line-height:17px;text-align:justify}
.f1{left:0;top:52px}.f2{left:257px;top:52px}.f3{left:0;top:177px}.f4{left:257px;top:177px}
.art div{position:absolute;width:95px;height:95px;border-radius:50%}

.payees{position:absolute;left:0;top:952px;width:997px;height:163px;background:var(--band);text-align:center}
.payees h2{color:var(--green);padding-top:19px;font-size:20px}
.payee-types{display:flex;justify-content:center;gap:56px;margin-top:15px;font-size:15px;font-weight:600;color:#444;line-height:30px}
.payee-types span{display:flex;align-items:center;gap:6px}
.payee-list{font-size:10px;font-weight:600;line-height:17px;color:#555;margin:10px auto 0;width:730px}

.site-footer{position:absolute;left:0;top:1115px;width:997px;text-align:center}
.site-footer .copy{font-size:10.5px;color:#555;margin-top:10px}
.site-footer .links{font-size:9.3px;color:var(--muted);line-height:14px;margin-top:6px}
</style>
</head>
<body>
<div class="page">
  <header class="site-header">
    <div class="wrap">
      <div class="brand">
        <div class="brand-name">nine-parts.com</div>
        <div class="brand-tag">"Bills Paid Fast"</div>
      </div>
      <div class="contact">
        <div>Call Us<strong>800.555.0199</strong></div>
        <div class="sep">Email Us<strong>info@nine-parts.com</strong></div>
      </div>
      <div class="header-rule"></div>
      <ul class="nav">
        <li class="active">Home</li>
        <li>The Story</li>
        <li>Why 9parts.com</li>
        <li>Are you eligible?</li>
        <li>Members</li>
        <li>Clients</li>
      </ul>
    </div>
  </header>

  <div class="hero" role="img" aria-label="Photo of a hand typing on a laptop keyboard"></div>

  <main class="content">
    <section class="welcome">
      <h2>Welcome to <span class="accent">nine-parts.com</span></h2>
      <p>Lorem ipsum dolor sit amet, consectetur adipiscing elit. Aenean facilisis libero tempus velit sodales, ac tristique eros tempus. Nullam molestie sapien ac eleifend aliquet. Suspendisse felis mauris, auctor vitae lacinia blandit, congue eu mi. Duis vel metus sed lacus convallis lobortis at ut leo. Maecenas gravida ipsum enim, at mollis tellus tempor eget. Sed ut arcu et leo luctus porta quis et leo. Curabitur ac lorem neque. <a href="#">Read More</a></p>
      <a class="btn">Get Started Now</a>
    </section>

    <section class="calc">
      <h2>How Much Do I Have to Payback?</h2>
      <div class="calc-row">
        <div>Enter Amount of Loan: $ ____________<small>Min $300-Max $700</small></div>
        <div>12 payments of:$ ____________ / month</div>
        <div>Total Paid Back:$____________</div>
      </div>
      <div class="calc-notes">
        It's that easy!<br>
        Once approved you will receive a confirmation number and your creditor will be funded within 72 hours<br>
        *Need referral number to get actual calculations
      </div>
    </section>

    <section class="features">
      <h2>One place for your bills. Paid.</h2>
      <div class="feature f1">
        <h3><svg width="20" height="22" viewBox="0 0 20 22"><path d="M10 1a7 7 0 0 0-7 7c0 5 7 12 7 12s7-7 7-12a7 7 0 0 0-7-7z" fill="#4cae4f"/><circle cx="10" cy="8" r="2.6" fill="#fff"/></svg>Easy &amp; organized just for you.</h3>
        <p>Morbi ornare convallis sollicitudin. Mauris diam enim, bibendum placerat justo ac, tempor rutrum justo. Sed semper ac tellus ut ultricies. Praesent dolor diam</p>
      </div>
      <div class="feature f2">
        <h3><svg width="24" height="20" viewBox="0 0 24 20"><path d="M2 6h7M0 10h7M3 14h6" stroke="#4cae4f" stroke-width="1.6"/><path d="M10 10l5-4 4 3-3 4 2 5M15 6l-2 6-4 5" stroke="#4cae4f" stroke-width="2.2" fill="none" stroke-linecap="round"/><circle cx="18" cy="3" r="2.2" fill="#4cae4f"/></svg>Faster than a speeding bullet.</h3>
        <p>Morbi ornare convallis sollicitudin. Mauris diam enim, bibendum placerat justo ac, tempor rutrum justo. Sed semper ac tellus ut ultricies. Praesent dolor diam</p>
      </div>
      <div class="feature f3">
        <h3><svg width="22" height="22" viewBox="0 0 22 22"><circle cx="11" cy="11" r="10" fill="#4cae4f"/><path d="M9 5v8h6" stroke="#fff" stroke-width="2.2" fill="none"/></svg>Real-time alerts and reminders.</h3>
        <p>Morbi ornare convallis sollicitudin. Mauris diam enim, bibendum placerat justo ac, tempor rutrum justo. Sed semper ac tellus ut ultricies. Praesent dolor diam</p>
      </div>
      <div class="feature f4">
        <h3><svg width="22" height="20" viewBox="0 0 22 20"><path d="M1 10L11 2l10 8" stroke="#4cae4f" stroke-width="2.4" fill="none"/><path d="M4 10v9h14v-9l-7-5z" fill="#4cae4f"/><rect x="9" y="13" width="4" height="6" fill="#fff"/></svg>Security and peace of mind.</h3>
        <p>Morbi ornare convallis sollicitudin. Mauris diam enim, bibendum placerat justo ac, tempor rutrum justo. Sed semper ac tellus ut ultricies. Praesent dolor diam</p>
      </div>
      <div class="art">
        <div role="img" aria-label="Illustration of hands holding a tablet showing an online shop" style="background:#6ab7e6;left:510px;top:61px"></div>
        <div role="img" aria-label="Illustration of a hand holding a phone with a shopping bag" style="background:#f26a2e;left:619px;top:61px"></div>
        <div role="img" aria-label="Illustration of a tablet with a magnifying glass over a product" style="background:#7ab648;left:506px;top:172px"></div>
        <div role="img" aria-label="Illustration of a laptop with a buy button and parcel" style="background:#fbd376;left:618px;top:172px"></div>
      </div>
    </section>
  </main>

  <section class="payees">
    <h2>Who Else Can I Pay?</h2>
    <div class="payee-types">
      <span><svg width="30" height="30" viewBox="0 0 30 30"><circle cx="15" cy="15" r="13.5" fill="none" stroke="#4cae4f" stroke-width="2"/><path d="M12 8c-3 5-4 7-4 9a4 4 0 0 0 8 0c0-2-1-4-4-9z M19 12c-2 3-3 5-3 6a3 3 0 0 0 6 0c0-1-1-3-3-6z" fill="#4cae4f"/></svg>Utilities</span>
      <span><svg width="30" height="30" viewBox="0 0 30 30"><circle cx="15" cy="15" r="13.5" fill="none" stroke="#4cae4f" stroke-width="2"/><path d="M11 7v5M19 7v5M9 12h12v4a6 6 0 0 1-12 0zM15 22v6" stroke="#4cae4f" stroke-width="2.4" fill="#4cae4f"/></svg>Cable</span>
      <span><svg width="30" height="30" viewBox="0 0 30 30"><rect x="3" y="2" width="13" height="26" rx="2" fill="#4cae4f"/><rect x="5" y="6" width="9" height="15" fill="#fff"/><path d="M13 12l8 0 0-4 8 8-8 8 0-4-8 0z" fill="#4cae4f" stroke="#fff" stroke-width="1"/></svg>Cell Phone</span>
      <span><svg width="34" height="30" viewBox="0 0 34 30"><path d="M7 12l3-7h14l3 7" stroke="#4cae4f" stroke-width="2.6" fill="none"/><rect x="3" y="12" width="28" height="10" rx="2" fill="#4cae4f"/><rect x="5" y="21" width="5" height="5" fill="#4cae4f"/><rect x="24" y="21" width="5" height="5" fill="#4cae4f"/><circle cx="9" cy="17" r="2" fill="#fff"/><circle cx="25" cy="17" r="2" fill="#fff"/></svg>Insurance</span>
    </div>
    <p class="payee-list">Northline Tel, Brightwave Mobile, Skyplate TV, Riverstone Cable, Coyle, Harbor Gas &amp; Electric, Oakridge Mutual, Meridian Insurance, Vantel, Sunvale Edison, Gulfshore Power &amp; Light, Keystone Edison, Fieldhouse, Granite Mutual, Allway, Linkcast, SkyDirect, Harborline, Quillnet, Clearview Cable, Epochlink, Dashcell, and thousands more.</p>
  </section>

  <footer class="site-footer">
    <p class="copy">©2014 nine-parts.com. All rights reserved.</p>
    <p class="links">Metro Cell Pay Bill | Northline Tel Bill Pay | Riverstone Pay Bill | Epochlink Bill Pay<br>
    Cicada Wireless Pay Bill | Beacon Money Online Payment | Pay Bill Online Penbrook | Pay Gas Bill<br>
    Pay Water Bill | Mobile Banking | Pay Gas Bill | Online Banking</p>
  </footer>
</div>
</body>
</html>
```